Australian Software Consultancy needs new Business Card Design

Design Business Card based on existing design artefacts (attached). We are open to all designs. As its a 2 sided design and we thought it might be quite striking to have one side with a black background and te other side with a white background.

Target Market(s)

Financial Services mainly.

Industry/Entity Type

Business

Contact Information for Business Card

Name :
Position :
Email :

Requirements
Must have
• Funky design using our existing assets

```html
<!DOCTYPE html>
<html lang="en">
<head>
<meta charset="utf-8">
<title>Kestrel Code – Business Card</title>
<link rel="stylesheet" href="https://fonts.googleapis.com/css2?family=Ubuntu:wght@300;400;700&display=swap">
<style>
  :root {
    --brand-red: #e4232b;
    --ink: #1b1b1b;
    --muted: #6d6d6d;
    --paper: #ffffff;
    --night: #050505;
    --backdrop: #f1f1f1;
  }
  * { margin: 0; padding: 0; box-sizing: border-box; }
  html, body {
    width: 1200px; height: 873px; overflow: hidden;
    background: var(--backdrop);
    font-family: "Ubuntu", sans-serif;
  }
  .stage {
    position: relative; width: 1200px; height: 873px;
    display: flex; align-items: center; justify-content: center; gap: 60px;
  }
  .card {
    position: relative; width: 460px; height: 263px;
    box-shadow: 0 6px 18px rgba(0,0,0,0.18);
    overflow: hidden;
  }
  /* Front side */
  .card--front { background: var(--paper); }
  .brand-row {
    position: absolute; left: 28px; top: 28px; right: 0;
    display: flex; align-items: center;
  }
  .brand-square {
    width: 14px; height: 10px; background: var(--ink); margin-right: 7px;
  }
  .brand-name {
    font-weight: 700; font-size: 17px; letter-spacing: 0.5px;
    color: var(--ink); white-space: nowrap;
  }
  .brand-rule {
    flex: 1; height: 5px; background: var(--brand-red); margin-left: 8px; margin-top: 4px;
  }
  .person {
    position: absolute; left: 96px; top: 100px;
  }
  .person-name {
    font-weight: 700; font-size: 30px; letter-spacing: 3px; color: var(--ink);
  }
  .person-role {
    font-weight: 300; font-size: 14px; letter-spacing: 2.5px; color: var(--muted);
    margin-top: 4px;
  }
  .contact-band {
    position: absolute; left: 0; right: 0; bottom: 0; height: 26px;
    background: var(--brand-red);
    display: flex; align-items: center; padding-left: 28px;
  }
  .contact-email {
    font-size: 11px; letter-spacing: 0.6px; color: #ffd4d4;
  }
  /* Back side */
  .card--back {
    background: var(--night);
    display: flex; align-items: center; justify-content: center; gap: 12px;
  }
  .back-dot { width: 14px; height: 14px; border-radius: 50%; background: var(--brand-red); }
  .back-name {
    font-weight: 700; font-size: 26px; letter-spacing: 2px; color: var(--brand-red);
  }
</style>
</head>
<body>
  <main class="stage">
    <section class="card card--front" aria-label="Card front">
      <div class="brand-row">
        <span class="brand-square"></span>
        <span class="brand-name">KESTREL CODE</span>
        <span class="brand-rule"></span>
      </div>
      <div class="person">
        <p class="person-name">ALEX MARLOW</p>
        <p class="person-role">ACCOUNTANT</p>
      </div>
      <div class="contact-band">
        <span class="contact-email">AlexMarlow@kestrelcode.com</span>
      </div>
    </section>
    <section class="card card--back" aria-label="Card back">
      <span class="back-dot"></span>
      <span class="back-name">KESTREL CODE</span>
    </section>
  </main>
</body>
</html>
```